BTW Website

I'm looking to design a 1 page website for my email marketing business called 'Inbox Harvest Works.' The business will be designed to attract eCommerce clients in particular.

It will be a very simple website with my picture, a Subscribe area to capture email addresses (and send out lead magnet PDFs), and some basic copy and social media links, nothing fancy!

I will provide the profile picture and all related copy, looking to use the color green and have it fill up the entire screen.

Here's an example of a similar site I really like:

http://prosecraftacademy.example/

I'm just looking for the site to provide information about my email marketing services and make a personal connection with the site visitors.

Target Market(s)

eCommerce businesse customers

Industry/Entity Type

Business

Number of Pages Required

1 page

Font styles to use
Sans Serif

Colors
00a990
33b8a4
87cfc6
cfeae6

Requirements
Must have
• Hosted on HostPeak serviers (we can discuss this*)
• Full page layout (no left/right margins)
• Profile picture / Subscribe and Lead Magnet section above the fold
• Ability for me to supply all copy (against white background)
• Friendzy / Chirpo / WorkWeave social media icons at the bottom
• Footer section with simple text I will provide

```html
<!DOCTYPE html>
<html lang="en">
<head>
<meta charset="utf-8">
<title>Inbox Harvest Works</title>
<link rel="stylesheet" href="https://fonts.googleapis.com/css2?family=Fira+Sans+Extra+Condensed:wght@700&family=Open+Sans:wght@300;400;600;700&display=swap">
<style>
  :root {
    --green: #00a990;
    --green-mid: #33b8a4;
    --green-soft: #87cfc6;
    --green-pale: #cfeae6;
    --ink: #222;
    --text: #555;
    --border-dark: #1e2a28;
    --footer: #23252b;
    --footer-line: #3a3d44;
    --footer-text: #8a8d94;
    --card-border: #dcdcdc;
    --meta-bg: #f5f5f5;
  }
  * { box-sizing: border-box; margin: 0; padding: 0; }
  html, body { width: 996px; height: 1200px; overflow: hidden; background: #fff; }
  body { font-family: "Open Sans", sans-serif; color: var(--text); position: relative; }

  .hero { position: absolute; left: 0; top: 0; width: 996px; height: 390px; background: var(--green); }
  .hero__portrait {
    position: absolute; left: 147px; top: 80px; width: 254px; height: 310px;
    border-radius: 120px 120px 0 0;
    background: linear-gradient(180deg, #e0b59a 0%, #d2a487 40%, #5b5853 62%, #4a4844 100%);
  }
  .hero__content { position: absolute; left: 520px; top: 94px; width: 400px; text-align: center; }
  .hero__title {
    font-family: "Fira Sans Extra Condensed", sans-serif; font-weight: 700;
    font-size: 26px; line-height: 25px; color: #fff; letter-spacing: 0.2px;
  }
  .subscribe__input {
    display: block; width: 294px; height: 37px; margin: 15px auto 0 52px;
    background: #fff; border: 1px solid #e4e4e4; border-radius: 2px;
    font: 400 11px "Open Sans", sans-serif; color: #aaa; text-align: left; padding: 0 9px; line-height: 35px;
  }
  .subscribe__button {
    display: block; width: 154px; height: 42px; margin: 19px 0 0 112px;
    background: var(--green-mid); border: 2px solid var(--border-dark); border-radius: 2px;
    font: 400 10px "Open Sans", sans-serif; color: #fff; line-height: 38px; letter-spacing: 0.2px;
  }
  .hero__text { margin: 20px 0 0 12px; width: 372px; font-size: 10.3px; line-height: 18.4px; color: #fff; }

  .section-badge {
    position: absolute; height: 41px; background: var(--green-mid); border: 2px solid var(--border-dark);
    border-radius: 2px; font-family: "Fira Sans Extra Condensed", sans-serif; font-weight: 700;
    font-size: 21px; line-height: 37px; color: #fff; text-align: center; letter-spacing: -0.3px;
  }
  .badge--clients { left: 376px; top: 431px; width: 244px; }
  .badge--blog { left: 407px; top: 767px; width: 182px; }

  .testimonial { position: absolute; left: 190px; top: 493px; width: 616px; text-align: center; }
  .testimonial__quote { font-weight: 300; font-size: 17px; line-height: 25.6px; color: var(--text); }
  .testimonial__avatar {
    width: 58px; height: 58px; border-radius: 50%; margin: 21px auto 0;
    background: radial-gradient(circle at 50% 40%, #e3c3ad 0%, #c9a68f 45%, #8fa79e 80%, #dcdcdc 100%);
  }
  .testimonial__name { margin-top: 12px; font-weight: 700; font-size: 11px; color: var(--ink); }

  .blog-card {
    position: absolute; top: 829px; width: 198px; height: 231px;
    border: 2px solid var(--card-border); background: #fff;
  }
  .blog-card__image { height: 139px; }
  .image--office { background: linear-gradient(135deg, #d8d6d1 0%, #b9b3a8 45%, #3b3a39 75%, #6e6a64 100%); }
  .image--laptop { background: linear-gradient(160deg, #5e6570 0%, #c9ccd1 40%, #e6dcd2 65%, #7d7f84 100%); }
  .blog-card__date { margin-top: 11px; text-align: center; font-size: 8.8px; color: #4b6a7a; }
  .blog-card__title {
    margin-top: 5px; text-align: center; font-weight: 700; font-size: 9.6px; color: var(--ink);
    text-transform: uppercase;
  }
  .blog-card__meta {
    position: absolute; left: 0; right: 0; bottom: 0; height: 31px; background: var(--meta-bg);
    text-align: center; line-height: 31px; font-size: 7px; letter-spacing: 0.6px; color: #666;
    text-transform: uppercase;
  }
  .blog-card__meta b { color: #333; }

  .footer { position: absolute; left: 0; top: 1072px; width: 996px; height: 128px; background: var(--footer); }
  .social { position: absolute; top: 22px; left: 0; width: 996px; display: flex; justify-content: center; gap: 44px; }
  .social__link { display: flex; align-items: center; gap: 8px; font-weight: 700; font-size: 8.5px; letter-spacing: 0.8px; color: #fff; text-transform: uppercase; }
  .social__dot { width: 30px; height: 30px; border-radius: 50%; background: var(--green-mid); }
  .footer__rule { position: absolute; left: 0; top: 74px; width: 996px; height: 1px; background: var(--footer-line); }
  .footer__text { position: absolute; top: 82px; left: 0; width: 996px; text-align: center; font-size: 9.3px; line-height: 18.4px; color: var(--footer-text); }
</style>
</head>
<body>
  <header class="hero">
    <div class="hero__portrait" role="img" aria-label="Portrait of the owner in a grey t-shirt with arms crossed"></div>
    <div class="hero__content">
      <h1 class="hero__title">LOREM IPSUM DOLOR SIT AMET<br>CONSETETUR SADIPSCING ELITR</h1>
      <div class="subscribe__input">Enter Your Email Address</div>
      <div class="subscribe__button">CONNECT WITH ME</div>
      <p class="hero__text">Lorem ipsum dolor sit amet consetetur sadipscing elitr sed diam nonumy eirmod tempor invidunt ut labore et dolore magna aliquyam erat sed diam voluptua. At vero eos et accusam et justo duo dolores et ea rebum. Stet clita kasd gubergren no sea takimata sanctus est Lorem ipsum dolor sit amet.</p>
    </div>
  </header>

  <h2 class="section-badge badge--clients">WHAT CLIENTS ARE SAYING</h2>
  <section class="testimonial">
    <p class="testimonial__quote">Lorem ipsum dolor sit amet consetetur sadipscing elitr sed diam nonumy eirmod tempor invidunt ut labore. Duis autem vel eum iriure dolor in hendrerit in vulputate velit esse molestie consequat vel illum dolore eu feugiat nulla facilisis at vero eros et accumsan et iusto odio dignissim.</p>
    <div class="testimonial__avatar" role="img" aria-label="Client portrait"></div>
    <p class="testimonial__name">Lorem Ipsum</p>
  </section>

  <h2 class="section-badge badge--blog">LATEST FROM BLOG</h2>
  <article class="blog-card" style="left:66px">
    <div class="blog-card__image image--office" role="img" aria-label="Businessman working at a desk"></div>
    <p class="blog-card__date">January 22, 2017</p>
    <h3 class="blog-card__title">Dolore magna aliquyam erat</h3>
    <p class="blog-card__meta"><b>By</b> BTW <b>in</b> Online Marketing</p>
  </article>
  <article class="blog-card" style="left:288px">
    <div class="blog-card__image image--laptop" role="img" aria-label="Hands typing on a laptop showing a chart"></div>
    <p class="blog-card__date">January 22, 2017</p>
    <h3 class="blog-card__title">At vero eos et accusam justo</h3>
    <p class="blog-card__meta"><b>By</b> BTW <b>in</b> Online Marketing</p>
  </article>
  <article class="blog-card" style="left:510px">
    <div class="blog-card__image image--office" role="img" aria-label="Businessman working at a desk"></div>
    <p class="blog-card__date">January 22, 2017</p>
    <h3 class="blog-card__title">Stet clita kasd gubergren</h3>
    <p class="blog-card__meta"><b>By</b> BTW <b>in</b> Online Marketing</p>
  </article>
  <article class="blog-card" style="left:731px">
    <div class="blog-card__image image--laptop" role="img" aria-label="Hands typing on a laptop showing a chart"></div>
    <p class="blog-card__date">January 22, 2017</p>
    <h3 class="blog-card__title">Lorem ipsum dolor sit amet</h3>
    <p class="blog-card__meta"><b>By</b> BTW <b>in</b> Online Marketing</p>
  </article>

  <footer class="footer">
    <nav class="social">
      <span class="social__link"><span class="social__dot"></span>Friendzy</span>
      <span class="social__link"><span class="social__dot"></span>Chirpo</span>
      <span class="social__link"><span class="social__dot"></span>WorkWeave</span>
    </nav>
    <div class="footer__rule"></div>
    <p class="footer__text">Lorem ipsum dolor sit amet, consetetur sadipscing elitr, sed diam nonumy eirmod tempor<br>invidunt ut labore et dolore magna aliquyam erat, sed diam voluptua.</p>
  </footer>
</body>
</html>
```